Velbrin Redesign of Website

I require my webpage to look different but this is out with my current providers platform
I will benefit from designs that use my wording (this is extremely important). I appreciate there may be a lot of wording in some areas so i would be happy with "read more" in various places. The use of my face in photo is a must and my logo is also a must which can be found on m y website www.velbrinadhd.co.uk I do not want corporate feel, i would like a warm, authentic. personal and inviting feel.

```html
<!DOCTYPE html>
<html lang="en">
<head>
<meta charset="utf-8">
<title>The Story Behind Velbrin</title>
<link rel="stylesheet" href="https://fonts.googleapis.com/css2?family=Playfair+Display:wght@600;700&family=Montserrat:wght@400;500;600&family=Sacramento&display=swap">
<style>
:root{
  --forest:#2f4d42;
  --forest-soft:#3a594d;
  --ink:#1f2b27;
  --heading:#2e4a40;
  --cream:#f3ede4;
  --card:#faf6ef;
  --band:#dbe2d3;
  --mist:#dde6ea;
  --sage:#dce3d3;
  --line:#c9cfbf;
  --script:#2c3f5c;
}
*{box-sizing:border-box;margin:0;padding:0}
html,body{width:838px;height:1200px;overflow:hidden}
body{position:relative;background:var(--cream);font-family:"Montserrat",sans-serif;color:var(--ink)}

/* sidebar */
.sidebar{position:absolute;left:0;top:0;width:188px;height:1200px;background:var(--forest)}
.brand{height:170px;background:#fff;display:flex;align-items:center;justify-content:center;gap:8px;position:relative}
.brand::after{content:"";position:absolute;left:86px;bottom:-7px;border:8px solid transparent;border-top-color:#fff;border-bottom:0}
.brand-dot{width:14px;height:14px;border-radius:50%;background:var(--forest)}
.brand-name{font-family:"Playfair Display",serif;font-weight:700;font-size:26px;color:var(--forest)}
.nav{position:absolute;left:15px;top:221px;width:158px}
.nav-item{height:70px;margin-bottom:8px;background:var(--forest-soft);border-radius:3px;display:flex;align-items:center;gap:10px;padding-left:12px;color:#f4efe6;font-size:12.5px;line-height:1.3}
.nav-item svg{width:26px;height:26px;flex:none;stroke:currentColor;fill:none;stroke-width:1.4}
.nav-item.active{background:var(--card);color:var(--ink)}
.leaf-art{position:absolute;left:30px;top:740px;width:130px;height:390px;border-radius:60px 60px 10px 60px;background:linear-gradient(160deg,rgba(130,160,125,.45),rgba(90,125,100,.25))}

/* hero */
.hero-photo{position:absolute;left:470px;top:0;width:368px;height:324px;background:linear-gradient(180deg,#c9ccc7 0%,#9fb0a7 30%,#6f8f7e 55%,#4f6c4c 80%,#7e8a55 100%);-webkit-mask-image:linear-gradient(90deg,transparent 0,#000 30%);mask-image:linear-gradient(90deg,transparent 0,#000 30%)}
.title{position:absolute;left:220px;top:28px;font-family:"Playfair Display",serif;font-weight:700;font-size:38px;line-height:1.12;color:var(--heading)}
.tagline{position:absolute;left:220px;top:112px;font-family:"Sacramento",cursive;font-size:29px;line-height:1;color:var(--script)}
.rule{position:absolute;left:220px;top:186px;width:210px;height:1px;background:var(--line)}
.rule::after{content:"";position:absolute;left:98px;top:-3px;width:7px;height:7px;border-radius:50%;background:#b9c2ad}
.intro{position:absolute;left:220px;top:201px;width:270px}
.intro h2{font-family:"Playfair Display",serif;font-size:10.5px;color:var(--heading);margin-bottom:4px}
.intro p{font-size:7.6px;line-height:1.35;margin-bottom:5px}
.ribbon{position:absolute;left:220px;top:283px;width:276px;height:26px;display:flex;align-items:center}
.ribbon svg{width:26px;height:22px;flex:none;stroke:var(--forest);fill:none;stroke-width:1.4}
.ribbon span{flex:1;height:100%;background:var(--forest);color:#fff;font-size:7.6px;line-height:1.3;display:flex;align-items:center;padding-left:8px;clip-path:polygon(0 0,100% 0,96% 50%,100% 100%,0 100%)}

/* landscape sits behind cards */
.landscape{position:absolute;left:188px;top:1020px;width:650px;height:180px;background:linear-gradient(180deg,rgba(243,237,228,0) 0%,#c7d1cf 35%,#8fa596 65%,#5e7d62 100%)}

/* cards */
.card{position:absolute;left:220px;width:586px;background:var(--card);border-radius:8px}
.sec-title{font-family:"Playfair Display",serif;font-weight:600;font-size:21px;color:var(--heading);text-align:center;display:flex;align-items:center;justify-content:center;gap:12px}
.sec-title::before,.sec-title::after{content:"";width:90px;height:1px;background:var(--line)}
.ico{width:34px;height:34px;border-radius:50%;display:flex;align-items:center;justify-content:center;flex:none}
.ico svg{width:20px;height:20px;stroke:var(--heading);fill:none;stroke-width:1.3}
.ico.mist{background:var(--mist)}
.ico.sage{background:var(--sage)}
h3{font-family:"Playfair Display",serif;font-weight:700;font-size:9.2px;line-height:1.22;color:var(--heading)}
.body{font-size:7.4px;line-height:1.32}

.journey{top:324px;height:285px}
.journey .sec-title{margin-top:10px}
.jgrid{position:absolute;left:15px;top:42px;width:552px;display:grid;grid-template-columns:1fr 1fr;row-gap:10px}
.jitem{display:flex;gap:6px;padding-right:8px}
.jitem h3{margin-bottom:3px}
.jgrid .jitem:nth-child(2n){border-left:1px solid #e3e0d6;padding-left:14px}
.jgrid .jitem:nth-child(-n+2){padding-bottom:10px;border-bottom:1px solid #e3e0d6}
.belief{position:absolute;left:14px;top:229px;width:553px;height:41px;background:var(--band);border-radius:4px;display:flex;align-items:center;justify-content:center;text-align:center;padding:0 64px;font-family:"Playfair Display",serif;font-weight:600;font-size:9.2px;line-height:1.3;color:var(--heading)}

.why{top:619px;height:173px}
.why .sec-title{margin-top:10px}
.wgrid{position:absolute;left:8px;top:42px;width:570px;display:grid;grid-template-columns:repeat(4,1fr)}
.witem{text-align:center;padding:0 6px;display:flex;flex-direction:column;align-items:center;gap:6px}
.witem + .witem{border-left:1px solid #e3e0d6}

.path{top:801px;height:108px}
.path .sec-title{margin-top:7px}
.steps{position:absolute;left:12px;top:36px;width:562px;display:flex;justify-content:space-between}
.step{display:flex;flex-direction:column;align-items:center;text-align:center;font-size:7.4px;line-height:1.15;gap:4px;position:relative}
.step .ico{width:32px;height:32px}
.steps::before{content:"";position:absolute;left:30px;right:30px;top:16px;border-top:1.4px dotted #8a948a}
.w50{width:50px}.w60{width:62px}.w70{width:70px}.w74{width:76px}.w82{width:84px}.w46{width:46px}

.approach{top:917px;height:148px}
.approach .sec-title{margin-top:8px}
.approach .lead{text-align:center;font-size:7.6px;margin-top:1px}
.agrid{position:absolute;left:14px;top:47px;width:566px;display:grid;grid-template-columns:250px 1fr;column-gap:16px;row-gap:5px}
.aitem{display:flex;gap:6px;align-items:center}
.aitem h3{margin-bottom:1px}
.aitem .body{line-height:1.28}

/* closing */
.closing{position:absolute;left:188px;top:1072px;width:650px;text-align:center}
.closing .quote{font-family:"Sacramento",cursive;font-size:19px;color:var(--script)}
.closing p{font-size:7.6px;line-height:1.3;margin-top:6px}
.closing svg{margin-top:6px;width:26px;height:20px;stroke:var(--forest);fill:none;stroke-width:1.4}
</style>
</head>
<body>

<aside class="sidebar">
  <div class="brand"><span class="brand-dot"></span><span class="brand-name">Velbrin</span></div>
  <nav class="nav">
    <div class="nav-item active"><svg viewBox="0 0 24 24"><path d="M3 11l9-7 9 7M5 10v10h5v-6h4v6h5V10"/></svg><span>The Story<br>Behind Velbrin</span></div>
    <div class="nav-item"><svg viewBox="0 0 24 24"><circle cx="10" cy="11" r="6"/><path d="M14 4h7v5h-4l-2 2"/></svg><span>How Velbrin<br>Can Support You</span></div>
    <div class="nav-item"><svg viewBox="0 0 24 24"><circle cx="12" cy="12" r="9"/><circle cx="12" cy="12" r="4"/></svg><span>Organisation &amp;<br>Partnership</span></div>
    <div class="nav-item"><svg viewBox="0 0 24 24"><path d="M3 19h8V7H3zM13 19h8V7h-8z"/><circle cx="12" cy="4" r="2"/></svg><span>Resouces &amp;<br>Workbooks</span></div>
    <div class="nav-item"><svg viewBox="0 0 24 24"><rect x="3" y="6" width="18" height="13" rx="1"/><path d="M3 7l9 7 9-7"/></svg><span>Contact</span></div>
    <div class="nav-item"><svg viewBox="0 0 24 24"><path d="M5 3h10l4 4v14H5z"/><path d="M8 10h8M8 14h6"/></svg><span>Privacy Policy</span></div>
  </nav>
  <div class="leaf-art" role="img" aria-label="Soft watercolour leafy branch decoration"></div>
</aside>

<div class="hero-photo" role="img" aria-label="Portrait of the founder smiling outdoors beside a mountain lake and pine forest"></div>
<h1 class="title">The Story<br>Behind Velbrin</h1>
<div class="tagline">Helping others began with<br>understanding myself.</div>
<div class="rule"></div>
<section class="intro">
  <h2>My name is Morven Kestrel Hale, founder of Velbrin.</h2>
  <p>I am an ADHD coach and wellbeing practitioner with lived experience of <b>ADHD and autism (AuDHD)</b>.</p>
  <p>I combine professional expertise with real-life experience to offer compassionate, practical support that helps you better understand yourself, your brain and your wellbeing.</p>
</section>
<div class="ribbon"><svg viewBox="0 0 26 22"><path d="M13 19C4 13 2 9 4 5s7-3 9 1c2-4 7-5 9-1s0 8-9 14z"/></svg><span>You don't need to have everything figured out before<br>reaching out. We'll take things one step at a time, together.</span></div>

<div class="landscape" role="img" aria-label="Watercolour mountain valley with pine trees and a winding river"></div>

<section class="card journey">
  <h2 class="sec-title">My Journey</h2>
  <div class="jgrid">
    <div class="jitem"><div class="ico mist"><svg viewBox="0 0 24 24"><path d="M12 4c-4 0-7 3-7 7s3 8 7 9c4-1 7-5 7-9s-3-7-7-7zM12 4v16"/></svg></div><div><h3>My adult ADHD diagnosis came during a period of profound self-discovery following a mental health breakdown.</h3><p class="body">For many years, my ADHD went unrecognised and was treated only with antidepressants, which never addressed the underlying cause of my struggles. Learning about ADHD didn't cause my breakdown – it helped explain it.</p></div></div>
    <div class="jitem"><div class="ico sage"><svg viewBox="0 0 24 24"><path d="M4 12c0-3 4-3 8 0s8 3 8 0-4-3-8 0-8 3-8 0z"/></svg></div><div><h3>As my understanding grew, I recognised I am also autistic – something that is common alongside ADHD.</h3><p class="body">Around 50–70% of autistic people also have ADHD, and many adults only recognise the second neurotype once the first has been identified. This combined experience is often called AuDHD. For me, it brought even greater clarity.</p></div></div>
    <div class="jitem"><div class="ico sage"><svg viewBox="0 0 24 24"><rect x="5" y="5" width="14" height="12" rx="1"/><path d="M3 19h18M9 9l3-2 3 2"/></svg></div><div><h3>This personal journey inspired me to deepen my professional knowledge and training.</h3><p class="body">I qualified as an Integrative Counsellor (HNC) and then as a Health &amp; Wellbeing Coach through Open Meadow Academy (NHB-recognised), followed by specialist training in Autism, ADHD and Somatic Coaching.</p></div></div>
    <div class="jitem"><div class="ico mist"><svg viewBox="0 0 24 24"><path d="M12 12c-4-3-5-5-3-7s3 0 3 1c0-1 1-3 3-1s1 4-3 7zM5 13l4 6h6l4-6"/></svg></div><div><h3>These experiences strengthened my passion for helping neurodivergent individuals better understand their brains, develop self-compassion and find strategies that work.</h3><p class="body">I believe every brain deserves understanding, support and practical tools for wellbeing.</p></div></div>
  </div>
  <div class="belief">I believe learning never stops, and I continue to develop my knowledge in neurodiversity, wellbeing and mental health so I can offer the best possible support.</div>
</section>

<section class="card why">
  <h2 class="sec-title">Why Velbrin Was Created</h2>
  <div class="wgrid">
    <div class="witem"><div class="ico mist"><svg viewBox="0 0 24 24"><path d="M12 20v-9M12 11c-4 0-6-3-6-6 4 0 6 2 6 6zM12 11c4 0 6-3 6-6-4 0-6 2-6 6z"/></svg></div><h3>I wanted to offer the kind of support I wish I had when I was struggling.</h3><p class="body">A safe, welcoming space where neurodivergent people feel seen, understood and supported to thrive in their own way.</p></div>
    <div class="witem"><div class="ico sage"><svg viewBox="0 0 24 24"><rect x="4" y="8" width="16" height="11" rx="1"/><path d="M9 8V5h6v3"/></svg></div><h3>I believe in practical, lasting support.</h3><p class="body">I empower people with knowledge, strategies and tools they can continue using long after our work together has ended.</p></div>
    <div class="witem"><div class="ico mist"><svg viewBox="0 0 24 24"><circle cx="8" cy="9" r="2.5"/><circle cx="16" cy="9" r="2.5"/><path d="M4 19c0-4 8-4 8 0M12 19c0-4 8-4 8 0"/></svg></div><h3>I understand the reality of neurodivergent family life.</h3><p class="body">As a mother to three neurodivergent children, I have invaluable lived experience of advocacy, navigating systems and creating a calmer home life.</p></div>
    <div class="witem"><div class="ico sage"><svg viewBox="0 0 24 24"><path d="M12 17c-5-4-6-6-4-8s4 0 4 1c0-1 2-3 4-1s1 4-4 8z"/></svg></div><h3>My personal experiences and professional qualifications shape the compassionate, neuro-affirming approach at the heart of everything I do.</h3></div>
  </div>
</section>

<section class="card path">
  <h2 class="sec-title">My Path</h2>
  <div class="steps">
    <div class="step w50"><div class="ico sage"><svg viewBox="0 0 24 24"><path d="M4 19V10l8-5 8 5v9z"/></svg></div>Housing<br>Officer</div>
    <div class="step w60"><div class="ico mist"><svg viewBox="0 0 24 24"><circle cx="12" cy="11" r="6"/><path d="M9 11h6"/></svg></div>Mental Health<br>Breakdown</div>
    <div class="step w50"><div class="ico sage"><svg viewBox="0 0 24 24"><circle cx="11" cy="11" r="6"/><path d="M15.5 15.5L20 20"/></svg></div>ADHD<br>Diagnosis</div>
    <div class="step w70"><div class="ico mist"><svg viewBox="0 0 24 24"><path d="M6 12c0-3 3-3 6 0s6 3 6 0-3-3-6 0-6 3-6 0z"/></svg></div>Understanding<br>Autism (AuDHD)</div>
    <div class="step w74"><div class="ico sage"><svg viewBox="0 0 24 24"><rect x="5" y="8" width="14" height="11"/><path d="M9 19v-4h6v4"/></svg></div>Integrative<br>Counselling Study</div>
    <div class="step w70"><div class="ico mist"><svg viewBox="0 0 24 24"><rect x="6" y="4" width="12" height="16" rx="1"/><path d="M9 9h6M9 13h6"/></svg></div>Health &amp;<br>Wellbeing Coach<br>(NHB-recognised)</div>
    <div class="step w82"><div class="ico sage"><svg viewBox="0 0 24 24"><circle cx="12" cy="10" r="6"/><path d="M12 16v4"/></svg></div>Specialist Training in<br>Autism, ADHD &amp;<br>Somatic Coaching</div>
    <div class="step w46"><div class="ico mist"><svg viewBox="0 0 24 24"><path d="M3 19l6-9 4 5 3-4 5 8z"/></svg></div>Velbrin<br>Created</div>
  </div>
</section>

<section class="card approach">
  <h2 class="sec-title">The Velbrin Approach</h2>
  <p class="lead">Everything I offer through Velbrin has been chosen with purpose.</p>
  <div class="agrid">
    <div class="aitem"><div class="ico sage"><svg viewBox="0 0 24 24"><circle cx="12" cy="12" r="3"/><circle cx="12" cy="12" r="7"/></svg></div><div><h3>Lived &amp; Tested</h3><p class="body">Many strategies and tools come from my own family's journey. They are tried, tested and proven to make a difference in real life.</p></div></div>
    <div class="aitem"><div class="ico mist"><svg viewBox="0 0 24 24"><path d="M5 12a7 7 0 0 1 12-5M19 12a7 7 0 0 1-12 5"/><circle cx="12" cy="12" r="2"/></svg></div><div><h3>Individual, Not One-Size-Fits-All</h3><p class="body">Every neurodivergent person is unique. There is no single therapy or approach that works for everyone. I work alongside you to find what works for you.</p></div></div>
    <div class="aitem"><div class="ico mist"><svg viewBox="0 0 24 24"><circle cx="12" cy="12" r="7"/><path d="M5 12h14M12 5c3 3 3 11 0 14"/></svg></div><div><h3>Practical &amp; Sustainable</h3><p class="body">I focus on realistic, practical approaches that fit into your everyday life and support your wellbeing in a way that feels manageable and meaningful.</p></div></div>
    <div class="aitem"><div class="ico sage"><svg viewBox="0 0 24 24"><path d="M12 16c-4-3-5-5-3-7s3 0 3 1c0-1 1-3 3-1s1 4-3 7zM5 14l4 6h6l4-6"/></svg></div><div><h3>Compassionate &amp; Neuro-Affirming</h3><p class="body">I believe neurodivergent people deserve support that is centred around the individual – not around trying to fit into a world that wasn't designed with neurodivergent minds in mind.</p></div></div>
  </div>
</section>

<section class="closing">
  <div class="quote">Because sometimes the smallest changes can make the biggest difference.</div>
  <p>Whether you are looking to better understand yourself, develop new strategies,<br>receive practical support or simply have someone who understands,<br>I'm here for you.</p>
  <svg viewBox="0 0 26 20"><path d="M13 18C4 12 2 8 4 4s7-3 9 1c2-4 7-5 9-1s0 8-9 14z"/></svg>
</section>

</body>
</html>
```